PlayerMetricsHubOnline - Game Statistics and Achievement Tracking

I need a new modern design for an existing website.

The website is a project to track statistics and achievements for games (currently Vaporo Achievements/Stats and stats for Continental Hauler Pro 2 and Prairie Freight Commander).
I am currently expanding the site with other platforms (like QLV) and more games.
I am also adding a user registration/signin with user profiles to show off their achievements and stats across all platforms and games.

The current website is available at https://plymetrx.example/
To search for data you can use the username "pixeldorian" (without quotes).

The design should be modern and extendable and contain space for a logo.

The logo should match the project. It should combine Gaming with statistics.

Target Market(s)

Video game players

Number of Pages Required

5+ page

Font styles to use
Sans Serif

Requirements
Must have
• Basic Layout, User profile page (not yet available on live site), Search Page for Platforms/Games, Platform profile page, Dark theme

```html
<!DOCTYPE html>
<html lang="en">
<head>
<meta charset="utf-8">
<title>PlayerMetricsHubOnline</title>
<link href="https://fonts.googleapis.com/css2?family=Inter:wght@400;500;600;700&display=swap" rel="stylesheet">
<style>
:root{
  --bg:#1c1c1c;
  --nav:#0b0b0b;
  --panel:#0e0e0e;
  --card:#0d0d0d;
  --footer:#0f0f0f;
  --blue:#1f63f0;
  --blue-band:#1d63ef;
  --white:#ffffff;
  --muted:#cfcfcf;
}
*{box-sizing:border-box;margin:0;padding:0}
html,body{width:1200px;height:3643px;overflow:hidden}
body{background:var(--bg);color:var(--white);font-family:"Inter",Arial,sans-serif;position:relative}
.abs{position:absolute}

/* nav */
.site-nav{position:absolute;left:0;top:0;width:1200px;height:74px;background:var(--nav)}
.brand{position:absolute;left:133px;top:24px;font-size:23px;font-weight:600;color:var(--white)}
.nav-links{position:absolute;left:490px;top:28px;display:flex;gap:17px;font-size:13px}
.nav-signin{position:absolute;left:901px;top:28px;font-size:13px;text-decoration:underline}
.nav-login{position:absolute;left:959px;top:24px;width:75px;height:27px;border-radius:5px;background:var(--blue);font-size:13px;display:flex;align-items:center;justify-content:center}
.nav-search{position:absolute;left:1050px;top:27px}

/* hero */
.hero{position:absolute;left:0;top:74px;width:1200px;height:577px;border-radius:0 0 57px 57px;overflow:hidden;
  background:
   radial-gradient(ellipse 320px 260px at 900px 290px,rgba(230,40,170,.85),transparent 70%),
   radial-gradient(ellipse 380px 300px at 1080px 140px,rgba(150,50,220,.7),transparent 70%),
   radial-gradient(ellipse 300px 200px at 80px 220px,rgba(90,110,200,.55),transparent 70%),
   linear-gradient(90deg,#2a1e2c 0%,#3b2236 45%,#6b1d5c 75%,#4a1650 100%)}
.hero-shade{position:absolute;inset:0;background:linear-gradient(90deg,rgba(0,0,0,.35),rgba(0,0,0,.05))}
.hero-brand{position:absolute;left:201px;top:232px;font-size:29px;font-weight:500}
.hero-title{position:absolute;left:200px;top:270px;font-size:51px;font-weight:500;letter-spacing:.3px}
.hero-sub{position:absolute;left:201px;top:343px;font-size:20px;line-height:28px;width:330px}

/* search panel */
.search-panel{position:absolute;left:191px;top:495px;width:816px;height:198px;background:var(--panel);border-radius:4px}
.search-panel h2{position:absolute;left:51px;top:38px;font-size:25px;font-weight:700}
.search-bar{position:absolute;left:47px;top:88px;width:726px;height:55px;background:#fff;border-radius:4px}
.search-bar .field{position:absolute;left:23px;top:17px;font-size:18px;color:#777}
.search-bar .divider{position:absolute;left:381px;top:8px;width:1px;height:40px;background:#ccc}
.search-bar .platforms{position:absolute;left:405px;top:21px;font-size:13px;color:#888}
.search-bar .caret{position:absolute;left:564px;top:25px;border:5px solid transparent;border-top-color:#555}
.search-btn{position:absolute;left:556px;top:6px;width:163px;height:43px;background:var(--blue);border-radius:4px;display:flex;align-items:center;justify-content:center;gap:7px;font-size:15px}
.adv-link{position:absolute;right:52px;top:154px;font-size:12px;color:var(--blue);text-decoration:underline}

/* results */
.section-title{font-size:31px;font-weight:500}
.results-title{position:absolute;left:143px;top:806px}
.sort-label{position:absolute;left:700px;top:815px;font-size:13px}
.sort-select{position:absolute;left:774px;top:804px;width:284px;height:38px;background:#fff;border-radius:3px;overflow:hidden}
.sort-select span{position:absolute;left:17px;top:12px;font-size:12px;color:#333}
.sort-select i{position:absolute;right:0;top:0;width:44px;height:38px;background:var(--blue)}
.sort-select i:after{content:"";position:absolute;left:16px;top:16px;border:6px solid transparent;border-top-color:#fff}

.card-grid{position:absolute;left:120px;display:grid;grid-template-columns:repeat(4,225px);column-gap:20px;row-gap:21px}
.results-grid{top:917px}
.release-grid{top:2304px}
.game-card{width:225px;height:230px;background:var(--card);position:relative}
.game-card .cover{height:107px}
.game-card h3{position:absolute;left:15px;top:118px;font-size:16px;font-weight:700}
.game-card p{position:absolute;left:15px;top:150px;font-size:12.5px;line-height:15px;width:200px}
.game-meta{position:absolute;left:15px;right:22px;top:197px;height:14px;display:flex;align-items:center;font-size:12.5px}
.os{display:inline-block;width:13px;height:12px;background:#fff;margin-right:4px}
.os.round{border-radius:50%;width:12px}
.sep{width:1px;height:13px;background:#fff;margin:0 15px 0 14px}
.play{margin-left:auto;background:var(--blue);border-radius:7px;font-size:9px;padding:2px 8px}

.load-more{position:absolute;left:542px;top:1960px;width:116px;height:27px;background:var(--blue);border-radius:4px;font-size:13px;display:flex;align-items:center;justify-content:center}

/* new release */
.release-band{position:absolute;left:0;top:2097px;width:1200px;height:559px;background:var(--blue-band)}
.release-title{position:absolute;left:127px;top:2222px;font-size:33px;font-weight:500}
.release-text{position:absolute;left:365px;top:2223px;width:550px;font-size:13px;line-height:20px}
.view-more{position:absolute;left:949px;top:2227px;width:109px;height:29px;background:#000;border-radius:5px;font-size:13px;display:flex;align-items:center;justify-content:center}

/* news */
.news-title{position:absolute;left:0;width:1200px;top:2742px;text-align:center;font-size:33px;font-weight:500}
.news-text{position:absolute;left:230px;width:740px;top:2800px;text-align:center;font-size:13px;line-height:20px}
.news-list{position:absolute;left:146px;top:2872px;display:flex;gap:28px}
.news-card{width:283px;position:relative;height:320px}
.news-card .photo{height:193px}
.news-meta{position:absolute;left:5px;top:211px;font-size:12px;color:var(--muted)}
.news-card h3{position:absolute;left:5px;top:240px;font-size:17px;font-weight:600;line-height:20px;width:280px}
.read-more{position:absolute;left:5px;top:292px;width:109px;height:26px;background:var(--blue);border-radius:3px;font-size:13px;display:flex;align-items:center;justify-content:center}

/* footer */
.site-footer{position:absolute;left:0;top:3297px;width:1200px;height:346px;background:var(--footer)}
.foot-brand{position:absolute;left:151px;top:99px;font-size:23px;font-weight:600}
.foot-about{position:absolute;left:151px;top:152px;width:240px;font-size:12.5px;line-height:16.5px}
.foot-heading{position:absolute;top:83px;font-size:25px;font-weight:500}
.foot-links{position:absolute;left:489px;top:127px;list-style:none;font-size:12.5px;line-height:24px}
.foot-sub{position:absolute;left:691px;top:124px;font-size:12px}
.news-form{position:absolute;left:688px;top:154px;width:341px;height:40px;background:#fff;border-radius:4px;overflow:hidden}
.news-form span{position:absolute;left:19px;top:12px;font-size:13px;color:#333}
.news-form b{position:absolute;right:0;top:0;width:126px;height:40px;background:var(--blue);font-weight:400;font-size:14px;color:#fff;display:flex;align-items:center;justify-content:center}
.socials{position:absolute;left:688px;top:223px;display:flex;gap:14px}
.socials i{width:20px;height:20px;border-radius:50%;background:#fff;display:block}
.foot-rule{position:absolute;left:91px;top:300px;width:1018px;height:1px;background:#888}
.copyright{position:absolute;left:0;width:1200px;top:317px;text-align:center;font-size:12.5px}
</style>
</head>
<body>

<header class="site-nav">
  <div class="brand">PlayerMetricsHubOnline</div>
  <nav class="nav-links"><span>Home</span><span>Vaporo</span><span>Games</span><span>About us</span></nav>
  <span class="nav-signin">Signin</span>
  <span class="nav-login">Login</span>
  <svg class="nav-search" width="20" height="20" viewBox="0 0 20 20" fill="none" stroke="#fff" stroke-width="1.6"><circle cx="8.5" cy="8.5" r="6.5"/><line x1="13.3" y1="13.3" x2="18.5" y2="18.5"/></svg>
</header>

<section class="hero" role="img" aria-label="Gaming desk lit in pink and purple with headphones and keyboard">
  <div class="hero-shade"></div>
</section>
<div class="hero-brand">PlayerMetricsHubOnline</div>
<h1 class="hero-title abs">Power Up and Play</h1>
<p class="hero-sub">The next challenge is waiting for you. Ready to conquer?</p>

<section class="search-panel">
  <h2>Search for Platforms/Games</h2>
  <div class="search-bar">
    <span class="field">Search</span>
    <span class="divider"></span>
    <span class="platforms">Platforms</span>
    <span class="caret"></span>
    <span class="search-btn"><svg width="16" height="16" viewBox="0 0 20 20" fill="none" stroke="#fff" stroke-width="2"><circle cx="8.5" cy="8.5" r="6.5"/><line x1="13.3" y1="13.3" x2="18.5" y2="18.5"/></svg>Search</span>
  </div>
  <span class="adv-link">Advance search</span>
</section>

<h2 class="section-title results-title">Search Result</h2>
<span class="sort-label">Sort by:</span>
<div class="sort-select"><span>Platforms</span><i></i></div>

<div class="card-grid results-grid">
  <article class="game-card"><div class="cover" role="img" aria-label="Game cover art" style="background:linear-gradient(135deg,#1f6e6a,#c9c94a 60%,#3a3a20)"></div><h3>Lunar Drift</h3><p>Lörem ipsum taliban-tv rack klimatångest prekiheten.</p><div class="game-meta"><i class="os"></i><i class="os round"></i><span class="sep"></span>RPG<span class="play">PLAY</span></div></article>
  <article class="game-card"><div class="cover" role="img" aria-label="Game cover art" style="background:linear-gradient(135deg,#2a4f8a,#3d8a3a 60%,#1b2b1b)"></div><h3>Lunar Drift</h3><p>Lörem ipsum taliban-tv rack klimatångest prekiheten.</p><div class="game-meta"><i class="os"></i><i class="os round"></i><span class="sep"></span>QLV<span class="play">PLAY</span></div></article>
  <article class="game-card"><div class="cover" role="img" aria-label="Game cover art" style="background:linear-gradient(135deg,#4b5560,#2a3038 60%,#596570)"></div><h3>Lunar Drift</h3><p>Lörem ipsum taliban-tv rack klimatångest prekiheten.</p><div class="game-meta"><i class="os"></i><i class="os round"></i><span class="sep"></span>RPG<span class="play">PLAY</span></div></article>
  <article class="game-card"><div class="cover" role="img" aria-label="Game cover art" style="background:linear-gradient(180deg,#7fb4e8,#c7dbef 60%,#8b9aa8)"></div><h3>Lunar Drift</h3><p>Lörem ipsum taliban-tv rack klimatångest prekiheten.</p><div class="game-meta"><i class="os"></i><i class="os round"></i><span class="sep"></span>QLV<span class="play">PLAY</span></div></article>

  <article class="game-card"><div class="cover" role="img" aria-label="Game cover art" style="background:linear-gradient(90deg,#1a2050,#3a2a6a 60%,#b0452a)"></div><h3>Lunar Drift</h3><p>Lörem ipsum taliban-tv rack klimatångest prekiheten.</p><div class="game-meta"><i class="os"></i><i class="os round"></i><span class="sep"></span>QLV<span class="play">PLAY</span></div></article>
  <article class="game-card"><div class="cover" role="img" aria-label="Game cover art" style="background:linear-gradient(180deg,#1a1a1a,#7a1414 55%,#2a2a2a)"></div><h3>Lunar Drift</h3><p>Lörem ipsum taliban-tv rack klimatångest prekiheten.</p><div class="game-meta"><i class="os"></i><i class="os round"></i><span class="sep"></span>RPG<span class="play">PLAY</span></div></article>
  <article class="game-card"><div class="cover" role="img" aria-label="Game cover art" style="background:linear-gradient(135deg,#3a3634,#6a5e58 50%,#2a1e1c)"></div><h3>Lunar Drift</h3><p>Lörem ipsum taliban-tv rack klimatångest prekiheten.</p><div class="game-meta"><i class="os"></i><i class="os round"></i><span class="sep"></span>QLV<span class="play">PLAY</span></div></article>
  <article class="game-card"><div class="cover" role="img" aria-label="Game cover art" style="background:linear-gradient(180deg,#1a1a1a 30%,#b4502a 60%,#4a2a1a)"></div><h3>Lunar Drift</h3><p>Lörem ipsum taliban-tv rack klimatångest prekiheten.</p><div class="game-meta"><i class="os"></i><i class="os round"></i><span class="sep"></span>RPG<span class="play">PLAY</span></div></article>

  <article class="game-card"><div class="cover" role="img" aria-label="Game cover art" style="background:linear-gradient(90deg,#4a3526,#2e2520 50%,#6a5a3a)"></div><h3>Lunar Drift</h3><p>Lörem ipsum taliban-tv rack klimatångest prekiheten.</p><div class="game-meta"><i class="os"></i><i class="os round"></i><span class="sep"></span>RPG<span class="play">PLAY</span></div></article>
  <article class="game-card"><div class="cover" role="img" aria-label="Game cover art" style="background:linear-gradient(135deg,#c8b890,#a06a30 50%,#5a5048)"></div><h3>Lunar Drift</h3><p>Lörem ipsum taliban-tv rack klimatångest prekiheten.</p><div class="game-meta"><i class="os"></i><i class="os round"></i><span class="sep"></span>QLV<span class="play">PLAY</span></div></article>
  <article class="game-card"><div class="cover" role="img" aria-label="Game cover art" style="background:linear-gradient(135deg,#0e1f4a,#2a4a9a 50%,#c02a3a)"></div><h3>Lunar Drift</h3><p>Lörem ipsum taliban-tv rack klimatångest prekiheten.</p><div class="game-meta"><i class="os"></i><i class="os round"></i><span class="sep"></span>RPG<span class="play">PLAY</span></div></article>
  <article class="game-card"><div class="cover" role="img" aria-label="Game cover art" style="background:linear-gradient(180deg,#9a7040,#c89a58 50%,#6a4a2a)"></div><h3>Lunar Drift</h3><p>Lörem ipsum taliban-tv rack klimatångest prekiheten.</p><div class="game-meta"><i class="os"></i><i class="os round"></i><span class="sep"></span>QLV<span class="play">PLAY</span></div></article>

  <article class="game-card"><div class="cover" role="img" aria-label="Game cover art" style="background:linear-gradient(135deg,#3a6a3a,#8aa04a 50%,#2a3a20)"></div><h3>Lunar Drift</h3><p>Lörem ipsum taliban-tv rack klimatångest prekiheten.</p><div class="game-meta"><i class="os"></i><i class="os round"></i><span class="sep"></span>RPG<span class="play">PLAY</span></div></article>
  <article class="game-card"><div class="cover" role="img" aria-label="Game cover art" style="background:linear-gradient(90deg,#141414 55%,#7a1a14)"></div><h3>Lunar Drift</h3><p>Lörem ipsum taliban-tv rack klimatångest prekiheten.</p><div class="game-meta"><i class="os"></i><i class="os round"></i><span class="sep"></span>QLV<span class="play">PLAY</span></div></article>
  <article class="game-card"><div class="cover" role="img" aria-label="Game cover art" style="background:linear-gradient(135deg,#6a8ab0,#d0d8e0 50%,#3a4a5a)"></div><h3>Lunar Drift</h3><p>Lörem ipsum taliban-tv rack klimatångest prekiheten.</p><div class="game-meta"><i class="os"></i><i class="os round"></i><span class="sep"></span>RPG<span class="play">PLAY</span></div></article>
  <article class="game-card"><div class="cover" role="img" aria-label="Game cover art" style="background:linear-gradient(135deg,#3a3e44,#1a1c20 50%,#5a5e64)"></div><h3>Lunar Drift</h3><p>Lörem ipsum taliban-tv rack klimatångest prekiheten.</p><div class="game-meta"><i class="os"></i><i class="os round"></i><span class="sep"></span>QLV<span class="play">PLAY</span></div></article>
</div>

<span class="load-more">Load More</span>

<section class="release-band"></section>
<h2 class="release-title">New Release</h2>
<p class="release-text">Lörem ipsum presa kroliga ifall fagån. Ninade telell seledes. Remurer sorade även om ber. Hembränd geost vöpred podat passivhus. Osen mononar, pofaska i beråssade.</p>
<span class="view-more">View More</span>

<div class="card-grid release-grid">
  <article class="game-card"><div class="cover" role="img" aria-label="Game cover art" style="background:linear-gradient(135deg,#a01a1a,#d84a3a 50%,#e0d8d0)"></div><h3>Lunar Drift</h3><p>Lörem ipsum taliban-tv rack klimatångest prekiheten.</p><div class="game-meta"><i class="os"></i><i class="os round"></i><span class="sep"></span>RPG<span class="play">PLAY</span></div></article>
  <article class="game-card"><div class="cover" role="img" aria-label="Game cover art" style="background:linear-gradient(135deg,#d0a020,#6a5a40 50%,#3a3a3a)"></div><h3>Lunar Drift</h3><p>Lörem ipsum taliban-tv rack klimatångest prekiheten.</p><div class="game-meta"><i class="os"></i><i class="os round"></i><span class="sep"></span>QLV<span class="play">PLAY</span></div></article>
  <article class="game-card"><div class="cover" role="img" aria-label="Game cover art" style="background:linear-gradient(135deg,#40a0e0,#d060c0 55%,#f0a0d0)"></div><h3>Lunar Drift</h3><p>Lörem ipsum taliban-tv rack klimatångest prekiheten.</p><div class="game-meta"><i class="os"></i><i class="os round"></i><span class="sep"></span>RPG<span class="play">PLAY</span></div></article>
  <article class="game-card"><div class="cover" role="img" aria-label="Game cover art" style="background:linear-gradient(135deg,#1a3a10,#5a9a20 50%,#2a4a14)"></div><h3>Lunar Drift</h3><p>Lörem ipsum taliban-tv rack klimatångest prekiheten.</p><div class="game-meta"><i class="os"></i><i class="os round"></i><span class="sep"></span>QLV<span class="play">PLAY</span></div></article>
</div>

<h2 class="news-title">Latest News</h2>
<p class="news-text">Lörem ipsum presa kroliga ifall fagån. Ninade telell seledes. Remurer sorade även om ber. Hembränd geost vöpred podat passivhus. Osen mononar, pofaska i beråssade.</p>

<div class="news-list">
  <article class="news-card"><div class="photo" role="img" aria-label="Player with headset at a gaming setup" style="background:linear-gradient(135deg,#1a2a3a,#3a5a7a 45%,#b02030 80%,#2a1a1a)"></div><div class="news-meta">Dec 16, 2024 &nbsp;&nbsp;|&nbsp;&nbsp; No Comments</div><h3>Velit dapibus sollicitudin sit iaculis ipsum dolor sit amet</h3><span class="read-more">Read More</span></article>
  <article class="news-card"><div class="photo" role="img" aria-label="Two players gaming in a purple-lit room" style="background:linear-gradient(135deg,#6a2ab0,#b040d0 50%,#2a1040)"></div><div class="news-meta">Dec 16, 2024 &nbsp;&nbsp;|&nbsp;&nbsp; No Comments</div><h3>Velit dapibus sollicitudin sit iaculis ipsum dolor sit amet</h3><span class="read-more">Read More</span></article>
  <article class="news-card"><div class="photo" role="img" aria-label="Player in red hoodie at a computer monitor" style="background:linear-gradient(135deg,#1a1a2a,#3a4a6a 45%,#c02020 80%,#3a0a0a)"></div><div class="news-meta">Dec 16, 2024 &nbsp;&nbsp;|&nbsp;&nbsp; No Comments</div><h3>Velit dapibus sollicitudin sit iaculis ipsum dolor sit amet</h3><span class="read-more">Read More</span></article>
</div>

<footer class="site-footer">
  <div class="foot-brand">PlayerMetricsHubOnline</div>
  <p class="foot-about">Lörem ipsum decinade reaskapet sörade det trafðning i sadade. Prektigt. Trasm trirad. Sofesam kavedir. Seskapet saföjäd då treskade.</p>
  <h3 class="foot-heading" style="left:488px">Company</h3>
  <ul class="foot-links"><li>Home</li><li>Vaporo</li><li>Games</li><li>About us</li><li>Contact us</li></ul>
  <h3 class="foot-heading" style="left:691px">Sign up to our newsletter</h3>
  <p class="foot-sub">Submit email and signup for monthly newsletters</p>
  <div class="news-form"><span>Email here...</span><b>Sign up</b></div>
  <div class="socials" aria-label="Social links"><i></i><i></i><i></i><i></i></div>
  <div class="foot-rule"></div>
  <p class="copyright">Copyright ©2024 PlayerMetricsHubOnline. All Rights Reserved.</p>
</footer>

</body>
</html>
```